Vesit cards for web development company

We need a business card design for our company. The company develops online platforms and conducts marketing consulting. Company logo. The cards must fit in with us (a junior start UP), but they must also be professional enough to impress with investors like banks. We wish you a combination of classic and modern design

Target Market(s)

Business partners and IT and marketing customers

Industry/Entity Type

It Company

Contact Information for Business Card

Folgende Information müssen Drauf.
Name, Position, Telefon Nr., Mobile Nr., E-Mail adresse, Optional sind noch Webadresse und HRB Nummer

Colors

Designer to choose colors to be used in the design.

Requirements
Must have
• The cards have to fit into the logo later and have to be dynamic and serious at the same time

```html
<!DOCTYPE html>
<html lang="en">
<head>
<meta charset="utf-8">
<title>Kestrel Development — Business Cards</title>
<link href="https://fonts.googleapis.com/css2?family=Roboto:wght@400;500;700&family=Roboto+Condensed:wght@700&display=swap" rel="stylesheet">
<style>
  :root {
    --backdrop: #8a6f58;
    --card: #1b1c1f;
    --brand-blue: #1a7cc4;
    --title-grey: #b5b7ba;
    --text-white: #f2f2f2;
    --web-grey: #5d5f63;
    --rule: rgba(255, 255, 255, 0.28);
  }
  * { margin: 0; padding: 0; box-sizing: border-box; }
  html, body {
    width: 1200px;
    height: 960px;
    overflow: hidden;
  }
  body {
    position: relative;
    background: var(--backdrop);
    font-family: "Roboto", Arial, sans-serif;
  }
  .card {
    position: absolute;
    width: 600px;
    height: 342px;
    background: var(--card);
    border-radius: 20px;
    box-shadow: 0 6px 14px rgba(0, 0, 0, 0.45);
    text-align: center;
  }
  .card--front { left: 315px; top: 113px; }
  .card--back  { left: 312px; top: 473px; }

  .brand {
    position: absolute;
    left: 0;
    right: 0;
    color: var(--brand-blue);
    font-family: "Roboto", Arial, sans-serif;
    font-weight: 700;
    text-transform: uppercase;
    line-height: 1;
  }
  .card--front .brand { top: 58px; font-size: 30px; letter-spacing: 0.04em; }
  .card--front .brand span { display: block; margin-bottom: 10px; }
  .card--back .brand { top: 112px; font-size: 42px; letter-spacing: 0.04em; }
  .card--back .brand span { display: block; margin-bottom: 14px; }

  .rule {
    position: absolute;
    left: 165px;
    width: 270px;
    height: 1px;
    background: linear-gradient(90deg, transparent, var(--rule) 40%, var(--rule) 60%, transparent);
  }
  .rule--top { top: 171px; }
  .rule--bottom { top: 248px; }

  .holder {
    position: absolute;
    top: 187px;
    left: 0;
    right: 0;
  }
  .holder__name {
    font-family: "Roboto Condensed", "Arial Narrow", sans-serif;
    font-weight: 700;
    font-size: 22px;
    color: var(--brand-blue);
    line-height: 1.1;
  }
  .holder__role {
    margin-top: 4px;
    font-size: 15px;
    font-weight: 500;
    color: var(--title-grey);
  }

  .contacts {
    position: absolute;
    top: 277px;
    left: 0;
    right: 0;
    font-size: 14px;
    color: var(--text-white);
  }
  .contacts .label { color: var(--brand-blue); }

  .website {
    position: absolute;
    top: 287px;
    left: 0;
    right: 0;
    font-size: 15px;
    letter-spacing: 0.45em;
    color: var(--web-grey);
  }
</style>
</head>
<body>
  <section class="card card--front">
    <div class="brand"><span>Kestrel</span><span>Development</span></div>
    <div class="rule rule--top"></div>
    <div class="holder">
      <p class="holder__name">JONAS WEBER</p>
      <p class="holder__role">CEO/FOUNDER</p>
    </div>
    <div class="rule rule--bottom"></div>
    <p class="contacts">
      <span class="label">M:</span> 614 205 7731
      <span class="label">C:</span> 742 390 1186
      <span class="label">E:</span> hello@kestreldev.com
    </p>
  </section>

  <section class="card card--back">
    <div class="brand"><span>Kestrel</span><span>Development</span></div>
    <p class="website">www.kestreldev.com</p>
  </section>
</body>
</html>
```